The Leadership Horizon Business Card

We need an attractive business card with the logo that we bought from ArtQuarry last year.
Our mission is to contribute to change the way today's leaders manage business companies bringing value to the workplace and helping them to build a new model of creating wealth.
Our logo is clear about our values : we seek Positive Change through People and are convinced that the pursuit of individual well-being and the chase of economic results can converge with the right management.
Industry/Entity Type
Management Consulting
Contact Information for Business Card
Corinne Valbrec
+34 612 80 27 35
corinne.valbrec@leadershiphorizonexample.com
www.leadershiphorizonexample.com
Look and feel
Each slider illustrates characteristics of the customer's brand and the style your logo design should communicate.

```html
<!DOCTYPE html>
<html lang="en">
<head>
<meta charset="utf-8">
<title>The Leadership Horizon – Business Card</title>
<link rel="stylesheet" href="https://fonts.googleapis.com/css2?family=Arimo:wght@400;700&family=Open+Sans:wght@400;600&display=swap">
<style>
  :root {
    --teal: #009a97;
    --teal-deep: #00817f;
    --teal-light: #3fae9c;
    --paper: #ffffff;
    --backdrop: #eceded;
    --ink-teal: #128f8c;
  }
  * { box-sizing: border-box; margin: 0; padding: 0; }
  html, body { width: 1200px; height: 720px; overflow: hidden; }
  body {
    background: var(--backdrop);
    font-family: "Open Sans", Arial, sans-serif;
    position: relative;
  }
  .card {
    position: absolute;
    top: 228px;
    width: 460px;
    height: 263px;
    overflow: hidden;
  }
  .card--front {
    left: 120px;
    background: linear-gradient(200deg, #00a6a3 0%, var(--teal) 45%, #008d8a 100%);
    color: var(--paper);
  }
  .card--back { left: 620px; background: var(--paper); }

  .brand-name {
    font-family: "Arimo", Arial, sans-serif;
    font-weight: 700;
    letter-spacing: 0.5px;
    white-space: nowrap;
  }
  .front-brand {
    position: absolute;
    top: 118px; left: 0; right: 0;
    display: flex; align-items: center; justify-content: center; gap: 10px;
  }
  .front-brand .brand-mark {
    width: 16px; height: 16px; border-radius: 50%; background: var(--paper);
  }
  .front-brand .brand-name { font-size: 21px; color: var(--paper); }
  .front-url {
    position: absolute;
    top: 207px; left: 0; right: 0;
    text-align: center;
    font-family: "Arimo", Arial, sans-serif;
    font-size: 11.5px;
  }

  .holder { position: absolute; top: 58px; left: 33px; color: var(--ink-teal); }
  .holder-name { font-family: "Arimo", Arial, sans-serif; font-weight: 700; font-size: 14.5px; }
  .holder-role { font-family: "Arimo", Arial, sans-serif; font-size: 12.5px; margin-top: 1px; }

  .back-brand {
    position: absolute; top: 70px; right: 40px;
    display: flex; align-items: center; gap: 6px;
  }
  .back-brand .brand-mark { width: 10px; height: 10px; border-radius: 50%; background: var(--ink-teal); }
  .back-brand .brand-name { font-size: 11.5px; color: var(--ink-teal); }

  .contact-list { position: absolute; top: 144px; left: 32px; list-style: none; }
  .contact-item {
    display: flex; align-items: center; gap: 9px;
    font-size: 10px; color: var(--ink-teal); height: 17px;
  }
  .contact-icon { width: 9px; height: 9px; fill: var(--ink-teal); flex: none; }

  .wave { position: absolute; left: 0; top: 0; }
</style>
</head>
<body>
  <section class="card card--front" aria-label="Business card front">
    <div class="front-brand">
      <span class="brand-mark"></span>
      <span class="brand-name">The Leadership Horizon</span>
    </div>
    <p class="front-url">www.leadershiphorizonexample.com</p>
  </section>

  <section class="card card--back" aria-label="Business card back">
    <div class="holder">
      <p class="holder-name">Corinne Valbrec</p>
      <p class="holder-role">President</p>
    </div>
    <div class="back-brand">
      <span class="brand-mark"></span>
      <span class="brand-name">The Leadership Horizon</span>
    </div>
    <ul class="contact-list">
      <li class="contact-item">
        <svg class="contact-icon" viewBox="0 0 10 10"><path d="M2 0.5 L3.6 2.6 L2.8 3.6 C3.4 5 4.6 6.3 6.2 7 L7.2 6.2 L9.4 7.8 L8.4 9.4 C4.4 9 0.8 5.4 0.5 1.6 Z"/></svg>
        <span>+34 612 80 27 35</span>
      </li>
      <li class="contact-item">
        <svg class="contact-icon" viewBox="0 0 10 10"><path d="M2.5 0 H7.5 V10 H2.5 Z M3.4 1 V8 H6.6 V1 Z"/></svg>
        <span>corinne.valbrec@leadershiphorizonexample.com</span>
      </li>
      <li class="contact-item">
        <svg class="contact-icon" viewBox="0 0 10 10"><path d="M0 2 H10 V8.5 H0 Z" /><path d="M0 2 L5 5.6 L10 2" stroke="#fff" stroke-width="0.9" fill="none"/></svg>
        <span style="font-weight:600">www.leadershiphorizonexample.com</span>
      </li>
    </ul>
    <svg class="wave" width="460" height="263" viewBox="0 0 460 263" aria-hidden="true">
      <path d="M0 245 C90 262 170 240 250 225 C330 208 390 200 460 212 L460 263 L0 263 Z" fill="var(--teal-light)"/>
      <path d="M0 255 C120 270 210 252 290 238 C360 226 420 222 460 230 L460 263 L0 263 Z" fill="var(--teal-deep)"/>
      <path d="M105 263 C200 252 270 236 330 226 C390 216 430 218 460 232" stroke="#ffffff" stroke-width="1" fill="none"/>
    </svg>
  </section>
</body>
</html>
```